Signal Post Hire Banner Ad Design Project

Hello Craft Throng,

We are looking for a banner ad that we can email to general contractors, and consulting firms in our service area to make them aware of our service.

We are an electrical contracting company based in Toronto, Ontario, Canada and one of divisions rents traffic light systems. We install our portable systems mainly in underground parking garages when construction restricts two way traffic to one lane. Our systems also get installed on ramps, and other areas that are under construction. Essentially, they allow phasing of big construction projects so the disruptions of traffic flow is kept to a minimal.
Our systems differ from other companies' rentals because our systems are cheaper, more reliable since they aren't wireless and they are LED (no bulbs burning out), we provide countdown lights that increase the effectiveness of the system and motorists' patience, and our systems adapt to rush hour traffic flow patterns at each site.
We have installed the systems at high profile locations throughout the city including The Marlow Quay Galleria, and Brinwick Mall.
We can provide job specific pricing or a monthly rate both of which include installation and removal.

I don't have very many good images of our systems but maybe you can photoshop our systems into another photo or a stock image might work as well.

More information on our systems can be found at www.fernholtvolt.example
Updates

Project Deadline Extended
Reason: Hi everyone, I am extending the deadline for submissions because I haven't had a proper chance to provide feedback to some of the designers who have submitted banner ads. I know it is frustrating when the deadline gets extended and I apologize. Thank you again and if I haven't provided feedback to you yet, please be patient because there have been some excellent designs that have been submitted so far. Dale

Project Deadline Extended
Reason: Still working with designers towards the right design.

Project Deadline Extended
Reason: I have been swamped with work and haven't been able to provide proper feedback to designers. Thanks for your patience, Dale

Industry/Entity Type

Construction

Requirements
Must have
• Fernholt Volt Logo

Focus on the fact that our systems are lower in price than our competitors or the fact that they are more cost effective.

Something that touches on the fact that our systems have countdown lights and adaptive control which increases traffic flow. This is a unique feature that no other company has.

```html
<!DOCTYPE html>
<html lang="en">
<head>
<meta charset="utf-8">
<title>Signal Post Hire – Banner Set</title>
<link rel="stylesheet" href="https://fonts.googleapis.com/css2?family=Arimo:ital,wght@0,400;0,700;1,700&display=swap">
<style>
  :root {
    --sheet: #ffffff;
    --ink-black: #0b0b0b;
    --orange: #f7941d;
    --orange-deep: #e35a0c;
    --amber-text: #f9a11b;
    --label-grey: #6b6b6b;
    --label-size-orange: #f28c1a;
    --btn-text: #3a1a05;
    --benefit-backdrop: rgba(0, 0, 0, 0.6);
  }
  html, body {
    margin: 0;
    width: 1200px;
    height: 1200px;
    overflow: hidden;
    background: var(--sheet);
    font-family: "Arimo", Arial, sans-serif;
  }
  .sheet { position: relative; width: 1200px; height: 1200px; }
  .banner { position: absolute; display: block; }
  .banner--leaderboard { left: 84px; top: 46px; width: 1019px; height: 126px; }
  .banner--rectangle { left: 87px; top: 256px; width: 420px; height: 350px; }
  .banner--skyscraper { left: 875px; top: 225px; width: 224px; height: 840px; }
  .spec {
    position: absolute;
    margin: 0;
    font-size: 21px;
    color: var(--label-grey);
    white-space: nowrap;
  }
  .spec__weight { color: var(--label-size-orange); }
  .spec--leaderboard { left: 94px; top: 178px; }
  .spec--rectangle { left: 84px; top: 616px; }
  .spec--skyscraper { left: 895px; top: 1080px; }
  .logo-name { font-family: "Arimo", Arial, sans-serif; font-weight: 400; fill: #ffffff; }
  .headline { font-family: "Arimo", Arial, sans-serif; font-weight: 700; fill: #ffffff; }
  .tagline { font-family: "Arimo", Arial, sans-serif; font-weight: 700; font-style: italic; fill: var(--amber-text); }
  .benefit { font-family: "Arimo", Arial, sans-serif; font-weight: 700; fill: #ffffff; }
  .benefit-backdrop { fill: var(--benefit-backdrop); }
  .cta-label { font-family: "Arimo", Arial, sans-serif; font-weight: 700; fill: var(--btn-text); }
</style>
</head>
<body>
<main class="sheet">

  <!-- 728 x 90 leaderboard -->
  <svg class="banner banner--leaderboard" viewBox="0 0 728 90" aria-label="Signal Post Hire leaderboard banner">
    <defs>
      <linearGradient id="lb-photo" x1="0" y1="0" x2="1" y2="1">
        <stop offset="0" stop-color="#3a3a3e"/><stop offset="0.45" stop-color="#6b5a3a"/><stop offset="1" stop-color="#2a2a2c"/>
      </linearGradient>
      <linearGradient id="lb-badge" x1="0" y1="0" x2="0" y2="1">
        <stop offset="0" stop-color="#e6e6e6"/><stop offset="1" stop-color="#8c8c8c"/>
      </linearGradient>
      <linearGradient id="lb-panel" x1="0" y1="0" x2="0" y2="1">
        <stop offset="0" stop-color="#000"/><stop offset="1" stop-color="#2b2b2b"/>
      </linearGradient>
      <linearGradient id="lb-btn" x1="0" y1="0" x2="0" y2="1">
        <stop offset="0" stop-color="#fbb040"/><stop offset="1" stop-color="#e35a0c"/>
      </linearGradient>
    </defs>
    <rect class="photo-area" x="130" y="0" width="400" height="90" fill="url(#lb-photo)" role="img" aria-label="Photo of a portable traffic light in an underground parking garage"/>
    <rect x="0" y="0" width="140" height="90" fill="var(--ink-black)"/>
    <path d="M140 0 Q120 45 140 90 L150 90 Q130 45 150 0 Z" fill="var(--orange)"/>
    <path d="M148 8 L330 8 L350 45 L330 82 L148 82 Q135 45 148 8 Z" fill="url(#lb-badge)" stroke="#6a6a6a" stroke-width="1"/>
    <path d="M153 13 L327 13 L344 45 L327 77 L153 77 Q142 45 153 13 Z" fill="none" stroke="#fff" stroke-width="1" stroke-dasharray="3 2"/>
    <text class="headline" x="240" y="41" font-size="22" text-anchor="middle">Signal Post</text>
    <text class="headline" x="240" y="66" font-size="22" text-anchor="middle">Hire</text>
    <g class="benefits">
      <rect class="benefit-backdrop" x="360" y="16" width="148" height="58" rx="4"/>
      <text class="benefit" x="434" y="33" font-size="11" text-anchor="middle">Lower cost than rivals</text>
      <text class="benefit" x="434" y="50" font-size="11" text-anchor="middle">LED countdown lights</text>
      <text class="benefit" x="434" y="67" font-size="11" text-anchor="middle">Adaptive traffic control</text>
    </g>
    <path d="M528 0 Q500 45 528 90 L728 90 L728 0 Z" fill="var(--orange)"/>
    <path d="M536 0 Q510 45 536 90 L728 90 L728 0 Z" fill="url(#lb-panel)"/>
    <rect x="57" y="12" width="14" height="14" fill="var(--orange)"/>
    <text class="logo-name" x="64" y="66" font-size="17" text-anchor="middle">Fernholt Volt</text>
    <text class="tagline" x="640" y="21" font-size="13" text-anchor="middle">For Construction Projects</text>
    <rect x="573" y="33" width="135" height="36" rx="3" fill="url(#lb-btn)"/>
    <text class="cta-label" x="626" y="57" font-size="16" text-anchor="middle">Click Here</text>
    <circle cx="689" cy="51" r="11" fill="#5a2200"/>
    <path d="M686 45 L694 51 L686 57 Z" fill="#fff"/>
  </svg>
  <p class="spec spec--leaderboard">728X90 <span class="spec__weight">24.0Kb</span></p>

  <!-- 300 x 250 medium rectangle -->
  <svg class="banner banner--rectangle" viewBox="0 0 300 250" aria-label="Signal Post Hire rectangle banner">
    <defs>
      <linearGradient id="mr-photo" x1="0" y1="0" x2="1" y2="1">
        <stop offset="0" stop-color="#2c2c30"/><stop offset="0.6" stop-color="#4a4a52"/><stop offset="1" stop-color="#7a5a2a"/>
      </linearGradient>
      <linearGradient id="mr-badge" x1="0" y1="0" x2="0" y2="1">
        <stop offset="0" stop-color="#e6e6e6"/><stop offset="1" stop-color="#8c8c8c"/>
      </linearGradient>
      <linearGradient id="mr-panel" x1="0" y1="0" x2="0" y2="1">
        <stop offset="0" stop-color="#000"/><stop offset="1" stop-color="#2b2b2b"/>
      </linearGradient>
      <linearGradient id="mr-btn" x1="0" y1="0" x2="0" y2="1">
        <stop offset="0" stop-color="#fbb040"/><stop offset="1" stop-color="#e35a0c"/>
      </linearGradient>
    </defs>
    <rect class="photo-area" x="0" y="70" width="300" height="120" fill="url(#mr-photo)" role="img" aria-label="Photo of a traffic light mounted in a parking garage ramp"/>
    <path d="M0 0 H300 V80 Q150 55 0 80 Z" fill="var(--ink-black)"/>
    <path d="M0 80 Q150 55 300 80 V90 Q150 65 0 90 Z" fill="var(--orange)"/>
    <rect x="143" y="5" width="14" height="14" fill="var(--orange)"/>
    <text class="logo-name" x="150" y="45" font-size="17" text-anchor="middle">Fernholt Volt</text>
    <path d="M20 82 L280 82 L280 116 L150 140 L20 116 Z" fill="url(#mr-badge)" stroke="#6a6a6a" stroke-width="1"/>
    <path d="M25 87 L275 87 L275 112 L150 135 L25 112 Z" fill="none" stroke="#fff" stroke-width="1" stroke-dasharray="3 2"/>
    <text class="headline" x="150" y="108" font-size="22" text-anchor="middle">Signal Post Hire</text>
    <g class="benefits">
      <rect class="benefit-backdrop" x="60" y="145" width="180" height="34" rx="4"/>
      <text class="benefit" x="150" y="159" font-size="11" text-anchor="middle">Lower cost · LED countdown lights</text>
      <text class="benefit" x="150" y="174" font-size="11" text-anchor="middle">Adaptive traffic control</text>
    </g>
    <path d="M0 190 Q150 170 300 190 V250 H0 Z" fill="var(--orange)"/>
    <path d="M0 197 Q150 177 300 197 V250 H0 Z" fill="url(#mr-panel)"/>
    <text class="tagline" x="150" y="202" font-size="13" text-anchor="middle">For Construction Projects</text>
    <rect x="93" y="211" width="135" height="36" rx="3" fill="url(#mr-btn)"/>
    <text class="cta-label" x="146" y="235" font-size="16" text-anchor="middle">Click Here</text>
    <circle cx="209" cy="229" r="11" fill="#5a2200"/>
    <path d="M206 223 L214 229 L206 235 Z" fill="#fff"/>
  </svg>
  <p class="spec spec--rectangle">300X250 <span class="spec__weight">23.1Kb</span></p>

  <!-- 160 x 600 skyscraper -->
  <svg class="banner banner--skyscraper" viewBox="0 0 160 600" aria-label="Signal Post Hire skyscraper banner">
    <defs>
      <linearGradient id="sk-photo" x1="0" y1="0" x2="0" y2="1">
        <stop offset="0" stop-color="#3a3a40"/><stop offset="0.5" stop-color="#5a4a34"/><stop offset="1" stop-color="#8a8a86"/>
      </linearGradient>
      <linearGradient id="sk-badge" x1="0" y1="0" x2="0" y2="1">
        <stop offset="0" stop-color="#8c8c8c"/><stop offset="0.5" stop-color="#cfcfcf"/><stop offset="1" stop-color="#8c8c8c"/>
      </linearGradient>
      <linearGradient id="sk-panel" x1="0" y1="0" x2="0" y2="1">
        <stop offset="0" stop-color="#000"/><stop offset="1" stop-color="#2b2b2b"/>
      </linearGradient>
      <linearGradient id="sk-btn" x1="0" y1="0" x2="0" y2="1">
        <stop offset="0" stop-color="#fbb040"/><stop offset="1" stop-color="#e35a0c"/>
      </linearGradient>
    </defs>
    <rect class="photo-area" x="0" y="100" width="160" height="380" fill="url(#sk-photo)" role="img" aria-label="Photo of a portable traffic signal with a single lane warning sign in a garage"/>
    <path d="M0 0 H160 V125 Q80 90 0 125 Z" fill="var(--ink-black)"/>
    <path d="M0 125 Q80 90 160 125 V138 Q80 103 0 138 Z" fill="var(--orange)"/>
    <rect x="73" y="12" width="14" height="14" fill="var(--orange)"/>
    <text class="logo-name" x="80" y="78" font-size="18" text-anchor="middle">Fernholt Volt</text>
    <path d="M8 125 Q80 92 152 125 V262 L80 300 L8 262 Z" fill="url(#sk-badge)" stroke="#6a6a6a" stroke-width="1"/>
    <path d="M14 130 Q80 100 146 130 V258 L80 293 L14 258 Z" fill="none" stroke="#fff" stroke-width="1" stroke-dasharray="3 2"/>
    <text class="headline" x="80" y="165" font-size="27" text-anchor="middle">Signal</text>
    <text class="headline" x="80" y="201" font-size="27" text-anchor="middle">Post</text>
    <text class="headline" x="80" y="237" font-size="27" text-anchor="middle">Hire</text>
    <g class="benefits">
      <rect class="benefit-backdrop" x="14" y="330" width="132" height="72" rx="4"/>
      <text class="benefit" x="80" y="350" font-size="12" text-anchor="middle">Lower Cost</text>
      <text class="benefit" x="80" y="371" font-size="12" text-anchor="middle">Countdown Lights</text>
      <text class="benefit" x="80" y="392" font-size="12" text-anchor="middle">Adaptive Control</text>
    </g>
    <path d="M0 482 Q80 456 160 482 V600 H0 Z" fill="var(--orange)"/>
    <path d="M0 490 Q80 464 160 490 V600 H0 Z" fill="url(#sk-panel)"/>
    <text class="tagline" x="80" y="510" font-size="16" text-anchor="middle">For Construction</text>
    <text class="tagline" x="80" y="532" font-size="16" text-anchor="middle">Projects</text>
    <rect x="10" y="552" width="142" height="38" rx="3" fill="url(#sk-btn)"/>
    <text class="cta-label" x="67" y="577" font-size="16" text-anchor="middle">Click Here</text>
    <circle cx="133" cy="571" r="11" fill="#5a2200"/>
    <path d="M130 565 L138 571 L130 577 Z" fill="#fff"/>
  </svg>
  <p class="spec spec--skyscraper">160X600 <span class="spec__weight">32.1Kb</span></p>

</main>
</body>
</html>
```